Web Design Project

We need a web design new company based in Australia. We're a search engine marketing company who predominantly manages Vexora bidlines campaigns.
Currently still deciding on a business name so lets use “Marlow Tappers” for now.
Target market....
small to medium size businesses
- more clicks to their website from the 1st page of Vexora
- more relevant, (higher quality) clicks
- higher return on investment from their bidlines campaign
- more sales, leads, (conversions)
We'd like clean, simple, semi-professional as we'd like to pick up some high end corporate clients.
A website that we love the look and feel of – but they’re a direct competitor so can’t be too similar in design.
http://www.brindlepath.com.au/search-engine-marketing.html
**please check portfolio on this web page..they designs are absolutely stunning!! http://www.brindlepath.com.au/website-design.html
Updates
Please refer to the attached file, a rough sketch of my web page.
place replace...."Afraid your bidlines campaign is underperforming with,....
Industry/Entity Type
Business
Look and feel

```html
<!DOCTYPE html>
<html lang="en">
<head>
<meta charset="utf-8">
<title>Business Name – Bidlines Management</title>
<link rel="stylesheet" href="https://fonts.googleapis.com/css2?family=Ubuntu:wght@300;400;500&family=PT+Sans+Narrow:wght@400;700&family=Arimo:wght@400&display=swap">
<style>
:root{
  --sky:#dbf2fd;
  --sky-pale:#ecf8fd;
  --coral:#f26a5c;
  --cream:#fdf3e6;
  --ink:#333a40;
  --grey:#8c8c8c;
  --grey-light:#aaa;
  --field:#e6e6e6;
  --orange:#ff6a21;
  --orange-top:#ff9a55;
  --tile-text:#b9cfdb;
  --rule:#c4c4c4;
}
*{margin:0;padding:0;box-sizing:border-box}
html,body{width:1200px;height:900px;overflow:hidden;background:#fff}
.page{position:relative;width:1200px;height:900px;font-family:"Arimo",Arial,sans-serif}
.header{position:absolute;left:0;top:4px;width:1200px;height:126px;background:var(--sky)}
.nav-band{position:absolute;left:0;top:130px;width:1200px;height:52px;background:var(--sky-pale)}
.logo{position:absolute;left:168px;top:50px;font:400 29px "Ubuntu",sans-serif;color:var(--ink);letter-spacing:-0.5px}
.logo span{color:var(--coral)}
.call{position:absolute;left:858px;top:0;width:198px;height:45px;background:#fff;border-radius:0 0 8px 8px;
  font:400 20px "PT Sans Narrow",sans-serif;color:var(--ink);padding:10px 0 0 24px}
.call strong{font-weight:700;font-size:21px}
.nav{position:absolute;top:147px;left:594px;display:flex;gap:0;list-style:none;font:400 16px "PT Sans Narrow",sans-serif;color:var(--ink)}
.nav li{margin-right:16px}
.nav li:last-child{margin-right:0}
.check-panel{position:absolute;left:480px;top:224px;width:569px;height:205px;border-radius:8px;
  background:linear-gradient(90deg,#fff 0%,#f6f6f6 35%,#f1f1f1 100%)}
.check-title{position:absolute;left:637px;top:262px;font:400 15px "PT Sans Narrow",sans-serif;color:var(--grey)}
.check-title .lead{font:300 22px "Ubuntu",sans-serif;color:#555;margin-left:8px}
.check-title .free{color:var(--orange)}
.url-field{position:absolute;left:616px;top:297px;width:397px;height:56px;background:var(--field);border-radius:6px;
  font:400 19px "PT Sans Narrow",sans-serif;color:#a3a3a3;padding:14px 0 0 22px}
.step-count{position:absolute;left:711px;top:379px;font:400 15px "PT Sans Narrow",sans-serif;color:var(--grey-light)}
.next-btn{position:absolute;left:782px;top:362px;width:88px;height:44px;border-radius:7px;
  background:linear-gradient(180deg,var(--orange-top),var(--orange));box-shadow:0 2px 3px rgba(0,0,0,.25);
  font:400 19px "PT Sans Narrow",sans-serif;color:#fff;text-align:center;line-height:43px}
.hero-circle{position:absolute;left:119px;top:117px;width:392px;height:392px;border-radius:50%;background:var(--coral);
  color:var(--cream);text-align:center;font-family:"Ubuntu",sans-serif}
.hero-circle .sub{position:absolute;top:124px;left:0;width:100%;font-weight:300;font-size:21px;line-height:29px}
.hero-circle .main{position:absolute;top:192px;left:0;width:100%;font-weight:400;font-size:32px;line-height:35px}
.services{position:absolute;top:534px;left:119px;width:940px}
.service{position:absolute;top:0;width:298px}
.service h2{font:400 19px "PT Sans Narrow",sans-serif;color:var(--ink);height:30px}
.service .visual{height:98px;background:var(--sky);display:flex;align-items:center;justify-content:center;
  font:400 15px "PT Sans Narrow",sans-serif;color:var(--tile-text)}
.service p{margin-top:9px;font-size:12.3px;line-height:17px;color:#555;text-align:justify}
.footer-rule{position:absolute;left:213px;top:811px;width:752px;height:1px;background:var(--rule)}
.copyright{position:absolute;left:212px;top:847px;font:400 13px "PT Sans Narrow",sans-serif;color:var(--grey)}
.social{position:absolute;left:798px;top:840px;display:flex;gap:5px;list-style:none}
.social li{width:24px;height:24px;border-radius:2px}
</style>
</head>
<body>
<div class="page">
  <header>
    <div class="header"></div>
    <div class="nav-band"></div>
    <div class="logo">Business <span>Name</span></div>
    <div class="call">Call : <strong>1300 482 905</strong></div>
    <ul class="nav">
      <li>Home</li><li>About</li><li>Vexora Bidlines</li><li>Other services</li><li>Why Choose us</li><li>Contact</li>
    </ul>
  </header>

  <section class="health-check">
    <div class="check-panel"></div>
    <div class="check-title">Step 1 : Website <span class="lead"><span class="free">Free</span> Bidlines Health Check</span></div>
    <div class="url-field">http://</div>
    <div class="step-count">Step 1 of 3</div>
    <div class="next-btn">Next</div>
  </section>

  <div class="hero-circle">
    <div class="sub">Want more sales and leads<br>from your bidlines campaign</div>
    <div class="main">WITHOUT INCREASING<br>YOUR BUDGET?</div>
  </div>

  <section class="services">
    <article class="service" style="left:0">
      <h2>Local Bidlines</h2>
      <div class="visual" role="img" aria-label="Image for local bidlines">Image goes here</div>
      <p>Lorem ipsum dolor sit amet, consectetur adipiscing elit. Aenean nec diam id nisi auctor posuere viverra sed tellus. Praesent nibh erat, consequat a vulputate et, rutrum eget lorem. Sed leo dui.</p>
    </article>
    <article class="service" style="left:320px">
      <h2>National Bidlines</h2>
      <div class="visual" role="img" aria-label="Image for national bidlines">Image goes here</div>
      <p>Lorem ipsum dolor sit amet, consectetur adipiscing elit. Aenean nec diam id nisi auctor posuere viverra sed tellus. Praesent nibh erat, consequat a vulputate et, rutrum eget lorem. Sed leo dui.</p>
    </article>
    <article class="service" style="left:639px">
      <h2>Ecommerce Bidlines</h2>
      <div class="visual" role="img" aria-label="Image for ecommerce bidlines">Image goes here</div>
      <p>Lorem ipsum dolor sit amet, consectetur adipiscing elit. Aenean nec diam id nisi auctor posuere viverra sed tellus. Praesent nibh erat, consequat a vulputate et, rutrum eget lorem. Sed leo dui.</p>
    </article>
  </section>

  <footer>
    <div class="footer-rule"></div>
    <div class="copyright">© 2012 Business Name. All rights reserved</div>
    <ul class="social" aria-label="Social links">
      <li style="background:#f9a33a"></li>
      <li style="background:#4f6fb5"></li>
      <li style="background:#5fb7e5"></li>
      <li style="background:#e27fb0"></li>
      <li style="background:#c9444f"></li>
      <li style="background:#4c86cf"></li>
    </ul>
  </footer>
</div>
</body>
</html>
```